Website for small historic hotel called the Corbett Crown

We are looking to design a website for a small Inn/Hotel.
Site would need to be able to take reservations and flow through to booking via Tallypay with orchard pay, quorra pay and zunmi pay (Chinese verson )
We would have links from Velora, Vorbo.com, roam critic etc to our website for booking purposes
Here are some examples of small inn/hotels doing the same sort of thing in our area. Provided purely for reference, not to be plagiarized!
https://innbrackwell.example/tollivers/
https://www.dunmorecourt.example/hotel
https://www.falconinnbrackwell.example/hotel
https://www.thewendover.example/
We will also provide you some photos, once the site has been done, to utilize instead of random shots taken from the internet as placeholders
I have also provided a link to some hotels in Perthshire Scotland which may also provide you with some ideas Again please do not plagiarise
https://glenvarrowlodge.example/
https://www.theinnatcraigbrannoch.example/
https://www.fennickheadhotel.example/
http://www.northern-hostelries.example/HighlandsandBorders.htm
Our inn is in Perth County in Ontario Canada NOT Scotland but the original owner was a Corbett from Perthshire Scotland and is responsible for the county being named Perth
We would need a landing page plus the following
page for rooms
Page for booking
Contact page
About US Page
Total site is landing page plus 4 or 5 sub pages
The general outline is provided. Please contact me with specific questions
Just as an update the folllowing are the placeholder names for the pages. They will be tabs at the top right and fllow through to sub pages off the main landing page
MAIN LANDING PAGE links at top to
1 _ history - the story of the building and Corbett
2_ Contact
3_ Rooms and Suites - will have each room and suite and link to sub-page for each
4 _ Perth County
5 - to be determined
The following would be sub pages
3 will display links to the suites: with a sub-page for each suite
Garden Suite - includes a 500 square foot patio and garden
Reception Suite - under renovation
Parlour Suite - Old parlor - Under renovation
GRAYMOORHAVEN Suite - Under renovation
1854 Suite 0- Under renovation
Updates
Just some additional information
The Inn/Hotel this website is for is named after a native of Perthshire Scotland who is also responsible for the area being names Perth County
The building is constructed in the 1850's and the decor and design are those of small-town inns you can find in the British Isles - England, Scotonal, Ireland and Wales
Some examples from Perthshire in Scotland - for inspiration, not plagiarisation!
https://glenvarrowlodge.example/
Please note the inn does not have a restaurant at present and only offers rooms
Feel free to submitt any questions for clarification
I have also provided a link to some hotels in Perthshire Scotland with similar designs and crests as well as to give you some background as to Perth. Again please do not plagiarise
https://glenvarrowlodge.example/
This is provided as an outline and we can answer specific questions
Few if any designs of any quality were received. Really nowhere near what was promised and certainly not the quality or quantity I would expect KT, whom I worked with before and I invited, submitted the bulk of the entries
Industry/Entity Type
boutique hotel - 19th century traditional British Isles
Number of Pages Required
5+ page
Look and feel
Each slider illustrates characteristics of the customer's brand and the style your logo design should communicate.

```html
<!DOCTYPE html>
<html lang="en">
<head>
<meta charset="utf-8">
<title>The Corbett Crown</title>
<link href="https://fonts.googleapis.com/css2?family=Inter:wght@400;500;600;700;800&display=swap" rel="stylesheet">
<style>
:root{
  --maroon:#3d0e0b;
  --gold:#d9b061;
  --sand:#d8cfc5;
  --taupe:#7b6256;
  --ink:#4a2a22;
  --muted:#c9b49a;
  --field:#dcdcdc;
  --white:#ffffff;
}
*{margin:0;padding:0;box-sizing:border-box}
html,body{width:1200px;height:3412px;overflow:hidden}
body{position:relative;font-family:'Inter',sans-serif;color:var(--ink);background:var(--white)}
.abs{position:absolute}

/* header */
.site-header{position:absolute;left:0;top:0;width:1200px;height:93px;background:var(--maroon);z-index:2}
.brand{position:absolute;left:127px;top:32px;color:var(--white);font-weight:700;font-size:14px;line-height:18px}
.nav{position:absolute;top:37px;display:flex;font-size:15px;color:#c4a59b}
.nav a{position:absolute;white-space:nowrap;color:inherit;text-decoration:none}
.nav .active{color:var(--white);font-weight:600}
.nav .active::after{content:"";position:absolute;left:-4px;right:-6px;top:24px;height:3px;background:var(--white)}
.btn{display:flex;align-items:center;justify-content:center;font-weight:500;text-decoration:none}
.btn-booking{position:absolute;left:958px;top:26px;width:116px;height:39px;background:var(--gold);color:var(--maroon);font-size:15px}

/* hero */
.hero{position:absolute;left:0;top:93px;width:1200px;height:584px;
  background:linear-gradient(90deg,#3f0f0c 0%,#5a2514 30%,#5b3a22 55%,#3b3a26 80%,#2b2a1e 100%)}
.hero-shade{position:absolute;inset:0;background:linear-gradient(180deg,rgba(0,0,0,0) 60%,rgba(40,45,50,.55) 100%)}
.hero h1{position:absolute;left:128px;top:190px;color:#f3ebe3;font-size:40px;font-weight:500;line-height:48px}
.hero .btn{position:absolute;top:302px;height:38px;font-size:15px}
.btn-gold{background:var(--gold);color:var(--maroon)}
.btn-stone{background:#8a6a58;color:#f3ebe3}

/* suites */
.suites{position:absolute;left:0;top:677px;width:1200px;height:580px;background:var(--sand)}
.section-title{position:absolute;color:var(--maroon);font-size:40px;font-weight:600}
.lead{position:absolute;color:var(--taupe);font-size:15px;line-height:18px}
.card{position:absolute;top:161px;width:254px;height:332px;background:var(--white);border-radius:9px;box-shadow:0 2px 8px rgba(0,0,0,.08)}
.card .photo{position:absolute;left:9px;top:8px;width:235px;height:171px;border-radius:4px;
  background:linear-gradient(180deg,#6ec7e6 0%,#9cbf8e 45%,#5e7d3c 70%,#8b7a6a 100%)}
.card h3{position:absolute;left:27px;top:187px;font-size:22px;font-weight:600;color:var(--maroon)}
.card p{position:absolute;left:27px;top:218px;width:200px;font-size:15px;line-height:18px;color:var(--muted)}
.card .link{position:absolute;left:27px;top:276px;font-size:14px;color:#c49a45;display:flex;align-items:center;gap:18px}
.circle-btn{position:absolute;width:40px;height:40px;border-radius:50%;background:var(--white);display:flex;align-items:center;justify-content:center}
.dots{position:absolute;display:flex;gap:8px}
.dots span{width:13px;height:13px;border-radius:50%;border:1.5px solid #b09a82}
.dots span.on{background:var(--gold);border-color:#c49a45}

/* about */
.about{position:absolute;left:0;top:1257px;width:1200px;height:638px;background:var(--white)}
.about .photo{position:absolute;left:683px;top:0;width:517px;height:638px;
  background:linear-gradient(180deg,#39b8ea 0%,#7cc0d8 22%,#6a8f4a 45%,#4f7a2c 75%,#7a6d55 100%)}
.body-copy{position:absolute;left:95px;width:462px;font-size:15px;line-height:18.2px;color:var(--ink)}

/* cta */
.cta{position:absolute;left:0;top:1895px;width:1200px;height:252px;background:var(--gold);text-align:center}
.cta h2{position:absolute;left:0;right:0;top:62px;font-size:40px;font-weight:600;color:var(--maroon)}
.btn-dark{background:var(--maroon);color:var(--gold)}
.cta .btn{position:absolute;left:510px;top:133px;width:179px;height:59px;font-size:20px}

/* reviews */
.reviews{position:absolute;left:0;top:2147px;width:1200px;height:429px;background:var(--sand)}
.rating{position:absolute;left:0;top:187px;width:351px;height:242px;background:var(--maroon)}
.stars{position:absolute;left:97px;top:50px;display:flex;gap:11px}
.score{position:absolute;left:97px;top:68px;font-size:82px;font-weight:600;color:var(--gold)}
.count{position:absolute;left:97px;top:170px;font-size:15px;font-weight:500;color:var(--gold)}
.quote-title{position:absolute;left:384px;top:216px;font-size:20px;font-weight:600;color:var(--taupe)}
.quote{position:absolute;left:384px;top:243px;width:734px;font-size:15px;line-height:18.2px;color:var(--taupe)}
.quote-by{position:absolute;right:82px;top:340px;font-size:12px;font-weight:600;color:var(--gold)}

/* contact */
.contact{position:absolute;left:0;top:2576px;width:1200px;height:560px;background:var(--white)}
.label{position:absolute;font-size:15px;color:var(--taupe)}
.field{position:absolute;height:58px;background:var(--field);border:2px solid #8f7265;font-size:14px;color:#bcbcbc;padding:17px 13px}
.contact .btn{position:absolute;left:195px;top:465px;width:266px;height:58px;font-size:20px;gap:18px}

/* footer */
.site-footer{position:absolute;left:0;top:3136px;width:1200px;height:276px;background:var(--maroon)}
.foot-brand{position:absolute;left:195px;top:64px;color:#f3ebe3;font-size:29px;font-weight:700;line-height:36px}
.foot-label{position:absolute;font-size:15px;color:#b8918a}
.foot-list{position:absolute;list-style:none;font-size:15px;color:#f1e7e0;line-height:26px}
.newsletter{position:absolute;left:193px;top:186px;width:226px;height:38px;border:2px solid #d9cfc9;background:var(--field);color:#bcbcbc;font-size:14px;padding:9px 12px}
.newsletter svg{position:absolute;right:8px;top:11px}
.copyright{position:absolute;left:0;right:0;top:248px;text-align:center;font-size:15px;color:#b8918a}
</style>
</head>
<body>

<header class="site-header">
  <div class="brand">The<br>Corbett Crown</div>
  <nav class="nav">
    <a class="active" href="#" style="left:417px">Home</a>
    <a href="#" style="left:498px">Suites
      <svg width="14" height="9" viewBox="0 0 14 9" style="margin-left:4px"><path d="M1 1l6 6 6-6" fill="none" stroke="#c4a59b" stroke-width="1.6"/></svg></a>
    <a href="#" style="left:603px">About Us</a>
    <a href="#" style="left:709px">Contact Us</a>
  </nav>
  <a class="btn btn-booking" href="#">Booking</a>
</header>

<section class="hero">
  <div class="abs" role="img" aria-label="Photo of a red-roofed white inn beside a lake, framed by autumn forest" style="inset:0"></div>
  <div class="hero-shade"></div>
  <h1>Take reservations<br>and booking via Tallypay</h1>
  <a class="btn btn-gold" href="#" style="left:128px;width:146px">Book your Inn</a>
  <a class="btn btn-stone" href="#" style="left:302px;width:134px">Contact Us</a>
</section>

<section class="suites">
  <h2 class="section-title" style="left:203px;top:44px">Your Suites</h2>
  <p class="lead" style="left:203px;top:102px;width:790px">Lorem ipsum is a long established fact that a reader will be distracted by the readable content of a page when looking at its layout</p>

  <div class="circle-btn" style="left:95px;top:307px"><svg width="22" height="12" viewBox="0 0 22 12"><path d="M21 6H2M7 1L2 6l5 5" fill="none" stroke="#3d0e0b" stroke-width="1.6"/></svg></div>
  <div class="circle-btn" style="left:1063px;top:307px"><svg width="22" height="12" viewBox="0 0 22 12"><path d="M1 6h19M15 1l5 5-5 5" fill="none" stroke="#3d0e0b" stroke-width="1.6"/></svg></div>

  <article class="card" style="left:193px">
    <div class="photo" role="img" aria-label="Photo of an ivy-covered Tudor-style house under blue sky"></div>
    <h3>Garden Suite</h3>
    <p>includes a 500 square foot patio and garden</p>
    <a class="link">Book your Inn <svg width="68" height="12" viewBox="0 0 68 12"><path d="M0 6h66M61 1l5 5-5 5" fill="none" stroke="#c49a45" stroke-width="1.8"/></svg></a>
  </article>
  <article class="card" style="left:473px">
    <div class="photo" role="img" aria-label="Photo of an ivy-covered Tudor-style house under blue sky"></div>
    <h3>Reception Suite</h3>
    <p>includes a 500 square foot patio and garden</p>
    <a class="link">Book your Inn <svg width="68" height="12" viewBox="0 0 68 12"><path d="M0 6h66M61 1l5 5-5 5" fill="none" stroke="#c49a45" stroke-width="1.8"/></svg></a>
  </article>
  <article class="card" style="left:752px">
    <div class="photo" role="img" aria-label="Photo of an ivy-covered Tudor-style house under blue sky"></div>
    <h3>Parlour Suite</h3>
    <p>includes a 500 square foot patio and garden</p>
    <a class="link">Book your Inn <svg width="68" height="12" viewBox="0 0 68 12"><path d="M0 6h66M61 1l5 5-5 5" fill="none" stroke="#c49a45" stroke-width="1.8"/></svg></a>
  </article>

  <div class="dots" style="left:573px;top:514px"><span class="on"></span><span></span><span></span></div>
</section>

<section class="about">
  <h2 class="section-title" style="left:96px;top:52px">About US</h2>
  <p class="body-copy" style="top:111px;color:var(--taupe)">Lorem ipsum is a long established fact that a reader will be distracted by the readable content of a page when looking at its layout</p>
  <p class="body-copy" style="top:216px">It is a long established fact that a reader will be distracted by the readable content of a page when looking at its layout. The point of using Lorem Ipsum is that it has a more-or-less normal distribution of letters, as opposed to using 'Content here, content here', making it look like readable English. Many desktop publishing packages and web page editors now use Lorem Ipsum as their default model text, and a search for 'lorem ipsum' will uncover many web sites still in their infancy</p>
  <p class="body-copy" style="top:400px">It is a long established fact that a reader will be distracted by the readable content of a page when looking at its layout. The point of using Lorem Ipsum is that it has a more-or-less normal distribution of letters, as opposed to using 'Content here, content here', making it look like readable English. Many desktop publishing packages and web page editors now use Lorem Ipsum as their default model text, and a search for 'lorem ipsum' will uncover many web sites still in their infancy</p>
  <div class="photo" role="img" aria-label="Photo of an ivy-covered Tudor-style inn with gables, chimney and garden"></div>
</section>

<section class="cta">
  <h2>Booking your inn now to reserve</h2>
  <a class="btn btn-dark" href="#">Book your Inn</a>
</section>

<section class="reviews">
  <h2 class="section-title" style="left:96px;top:53px">Reviews annd Comments</h2>
  <p class="lead" style="left:97px;top:110px;width:760px">Lorem ipsum is a long established fact that a reader will be distracted by the readable content of a page when looking at its layout</p>

  <div class="rating">
    <div class="stars">
      <svg width="22" height="21" viewBox="0 0 24 23"><path d="M12 1l3.2 7 7.6.8-5.7 5.1 1.6 7.5L12 17.6 5.3 21.4l1.6-7.5L1.2 8.8 8.8 8z" fill="#f5e63a"/></svg>
      <svg width="22" height="21" viewBox="0 0 24 23"><path d="M12 1l3.2 7 7.6.8-5.7 5.1 1.6 7.5L12 17.6 5.3 21.4l1.6-7.5L1.2 8.8 8.8 8z" fill="#f5e63a"/></svg>
      <svg width="22" height="21" viewBox="0 0 24 23"><path d="M12 1l3.2 7 7.6.8-5.7 5.1 1.6 7.5L12 17.6 5.3 21.4l1.6-7.5L1.2 8.8 8.8 8z" fill="#f5e63a"/></svg>
      <svg width="22" height="21" viewBox="0 0 24 23"><path d="M12 1l3.2 7 7.6.8-5.7 5.1 1.6 7.5L12 17.6 5.3 21.4l1.6-7.5L1.2 8.8 8.8 8z" fill="#f5e63a"/></svg>
      <svg width="22" height="21" viewBox="0 0 24 23"><path d="M12 1l3.2 7 7.6.8-5.7 5.1 1.6 7.5L12 17.6 5.3 21.4l1.6-7.5L1.2 8.8 8.8 8z" fill="#f5e63a"/></svg>
    </div>
    <div class="score">5.0</div>
    <div class="count">26665 Reviews</div>
  </div>

  <h3 class="quote-title">Lorem ipsum is a long established</h3>
  <p class="quote">Lorem ipsum is a long established fact that a reader will be distracted by the readable content of a page when looking at its layout Lorem ipsum is a long established fact that a reader will be distracted by the readable content of a page when looking at its layout Lorem ipsum is a long established fact that a reader will be distracted by the readable content of a page when looking at its layout Lorem ipsum is a long established fact that a reader will be distracted by the readable content of a page when looking</p>
  <div class="quote-by">Lorem ipsum is a long established</div>

  <div class="circle-btn" style="left:384px;top:367px"><svg width="22" height="12" viewBox="0 0 22 12"><path d="M21 6H2M7 1L2 6l5 5" fill="none" stroke="#3d0e0b" stroke-width="1.6"/></svg></div>
  <div class="circle-btn" style="left:466px;top:367px"><svg width="22" height="12" viewBox="0 0 22 12"><path d="M1 6h19M15 1l5 5-5 5" fill="none" stroke="#3d0e0b" stroke-width="1.6"/></svg></div>
  <div class="dots" style="left:1063px;top:389px;gap:7px"><span class="on"></span><span></span><span></span></div>
</section>

<section class="contact">
  <h2 class="section-title" style="left:96px;top:50px">Contact us</h2>
  <p class="lead" style="left:97px;top:110px;width:760px">Lorem ipsum is a long established fact that a reader will be distracted by the readable content of a page when looking at its layout</p>

  <label class="label" style="left:194px;top:184px">Email id</label>
  <div class="field" style="left:193px;top:208px;width:392px">Enter your email id</div>
  <label class="label" style="left:614px;top:184px">Phone Number</label>
  <div class="field" style="left:613px;top:208px;width:393px">Enter your Phone number</div>

  <label class="label" style="left:194px;top:295px">Comments</label>
  <div class="field" style="left:193px;top:318px;width:813px;height:110px">Enter your Message</div>

  <a class="btn btn-dark" href="#">Book your Inn <svg width="70" height="16" viewBox="0 0 70 16"><path d="M0 8h67M61 2l6 6-6 6" fill="none" stroke="#d9b061" stroke-width="2"/></svg></a>
</section>

<footer class="site-footer">
  <div class="foot-brand">The<br>Corbett Crown</div>
  <div class="foot-label" style="left:194px;top:164px">Sign&nbsp; up Newsletter</div>
  <div class="newsletter">Enter your email id
    <svg width="30" height="12" viewBox="0 0 30 12"><path d="M0 6h28M23 1l5 5-5 5" fill="none" stroke="#6b5a55" stroke-width="1.6"/></svg>
  </div>

  <div class="foot-label" style="left:600px;top:36px">Site Map</div>
  <ul class="foot-list" style="left:600px;top:76px">
    <li>Booking</li><li>Rooms</li><li>About Us</li><li>Cotact us</li><li>Privacy</li><li>Terms &amp; conditons</li>
  </ul>

  <div class="foot-label" style="left:922px;top:36px">Social Links</div>
  <ul class="foot-list" style="left:922px;top:76px">
    <li>Chatterly</li><li>Vidloom</li><li>Snapora</li>
  </ul>

  <div class="copyright">Copyright © 2022 The Corbett Crown</div>
</footer>

</body>
</html>
```